For lease banners for Businesses

I need to turn all of these banners into high quality graphics so I can get them printed on vinyl vertical banners that are 44"W x 88"H. So I need them most likely to be vector artwork, and ready to upload to a custom vinyl print shop.

```html
<!DOCTYPE html>
<html lang="en">
<head>
<meta charset="utf-8">
<title>Northgate Holdings – Leasing Now Banner</title>
<link href="https://fonts.googleapis.com/css2?family=Bebas+Neue&family=Great+Vibes&family=Montserrat:wght@500&family=Rubik:wght@500;600&display=swap" rel="stylesheet">
<style>
  :root {
    --page: #f4f4f4;
    --ink: #0a0a0a;
    --gold: #c39c48;
    --white: #ffffff;
    --photo-top: #23271d;
    --photo-mid: #3a3328;
  }
  * { box-sizing: border-box; margin: 0; padding: 0; }
  html, body {
    width: 1200px; height: 2323px; overflow: hidden;
    background: var(--page);
  }
  .banner {
    position: absolute; left: 122px; top: 206px;
    width: 957px; height: 1911px;
    background: var(--ink);
    overflow: hidden;
    color: var(--white);
  }
  .hero-photo {
    position: absolute; left: 0; top: 0; width: 100%; height: 1400px;
    background:
      radial-gradient(ellipse at 55% 62%, rgba(110,90,65,0.55), transparent 55%),
      linear-gradient(180deg, var(--photo-top) 0%, #2c2e24 35%, var(--photo-mid) 62%, #1a1815 82%, var(--ink) 100%);
  }
  .abs { position: absolute; }
  .headline {
    left: 0; width: 100%; text-align: center;
    font-family: "Bebas Neue", sans-serif; line-height: 1;
  }
  .headline .line { position: absolute; left: 0; width: 100%; white-space: nowrap; }
  .headline .l1 { top: 70px; font-size: 156px; }
  .headline .l2 { top: 190px; font-size: 196px; }
  .headline .l3 { top: 348px; font-size: 196px; }
  .rule { height: 3px; background: var(--gold); }
  .tagline {
    left: 0; width: 100%; text-align: center;
    font-family: "Great Vibes", cursive; color: var(--gold);
    font-size: 84px; line-height: 74px; top: 550px;
  }
  .features {
    top: 1030px; left: 0; width: 100%; height: 140px;
  }
  .feature {
    position: absolute; top: 0; width: 200px; margin-left: -100px;
    text-align: center;
    font-family: "Rubik", sans-serif; font-weight: 600;
    font-size: 24px; line-height: 31px; text-transform: uppercase;
  }
  .feature svg { display: block; margin: 0 auto 18px; width: 66px; height: 64px; }
  .brand {
    top: 1226px; left: 155px; height: 146px; display: flex; align-items: center;
  }
  .brand-square { width: 138px; height: 146px; border: 3px solid var(--gold); }
  .brand-divider { width: 2px; height: 146px; background: var(--gold); margin: 0 40px 0 36px; }
  .brand-name {
    font-family: "Montserrat", sans-serif; font-weight: 500; color: var(--white);
    text-transform: uppercase;
  }
  .brand-name .main { display: block; font-size: 56px; letter-spacing: 9px; line-height: 70px; }
  .brand-name .sub { display: block; font-size: 30px; letter-spacing: 17px; line-height: 50px; }
  .leasing {
    top: 1420px; left: 0; width: 100%; text-align: center;
    font-family: "Bebas Neue", sans-serif; color: var(--gold);
    font-size: 164px; line-height: 1; letter-spacing: 1px;
  }
  .contact {
    left: 126px; display: flex; align-items: center;
    font-family: "Rubik", sans-serif; font-weight: 600;
  }
  .contact svg { width: 54px; height: 50px; margin-right: 32px; }
  .contact.phone { top: 1604px; font-size: 52px; }
  .contact.email { top: 1680px; font-size: 38px; }
  .sectors {
    top: 1776px; left: 126px; width: 730px;
    display: flex; justify-content: space-between; align-items: center;
    font-family: "Rubik", sans-serif; font-weight: 500; font-size: 42px;
    text-transform: uppercase;
  }
  .sectors .dot { width: 17px; height: 17px; border-radius: 50%; background: var(--gold); }
</style>
</head>
<body>
<main class="banner">
  <div class="hero-photo" role="img" aria-label="Photo of friends sharing food and drinks at an outdoor table on a busy tree-lined downtown street with string lights"></div>

  <h1 class="abs headline">
    <span class="line l1">This could be</span>
    <span class="line l2">your next</span>
    <span class="line l3">location.</span>
  </h1>

  <div class="abs rule" style="top:529px;left:118px;width:720px;"></div>

  <p class="abs tagline">Build your business<br>where people gather.</p>

  <section class="abs features">
    <div class="feature" style="left:146px;">
      <svg viewBox="0 0 66 64" fill="none" stroke="var(--gold)" stroke-width="3"><path d="M33 62 C20 44 12 34 12 24 a21 21 0 0 1 42 0 c0 10-8 20-21 38z"/><circle cx="33" cy="24" r="8"/></svg>
      High<br>Visibility
    </div>
    <div class="feature" style="left:352px;">
      <svg viewBox="0 0 66 64" fill="none" stroke="var(--gold)" stroke-width="3"><circle cx="33" cy="16" r="10"/><path d="M14 60 v-10 a19 19 0 0 1 38 0 v10z"/><circle cx="12" cy="24" r="7"/><circle cx="54" cy="24" r="7"/><path d="M2 56 v-6 a11 11 0 0 1 14-10"/><path d="M64 56 v-6 a11 11 0 0 0-14-10"/></svg>
      Downtown<br>Traffic
    </div>
    <div class="feature" style="left:579px;">
      <svg viewBox="0 0 66 64" fill="none" stroke="var(--gold)" stroke-width="3"><rect x="4" y="2" width="58" height="60"/><path d="M30 2 v24 M4 26 h40 M44 26 v10 M44 48 v14 M4 44 h14 M26 44 h36 M18 44 v18"/></svg>
      Flexible<br>Floorplans
    </div>
    <div class="feature" style="left:800px;">
      <svg viewBox="0 0 66 64" fill="none" stroke="var(--gold)" stroke-width="3" stroke-linejoin="round"><path d="M2 22 l12-12 10 6 M64 22 l-12-12-14 6-10 8 a4 4 0 0 0 6 6 l10-6 14 14"/><path d="M14 10 l-10 12 M52 10 l10 12 M12 30 l18 20 a4 4 0 0 0 6-6 M24 40 l10 10 a4 4 0 0 0 6-6 M30 34 l12 12 a4 4 0 0 0 6-6 M54 38 l-6 4"/></svg>
      Local<br>Ownership
    </div>
  </section>

  <div class="abs brand">
    <div class="brand-square"></div>
    <div class="brand-divider"></div>
    <div class="brand-name">
      <span class="main">Northgate</span>
      <span class="sub">Holdings</span>
    </div>
  </div>

  <div class="abs rule" style="top:1406px;left:126px;width:720px;"></div>
  <h2 class="abs leasing">Leasing Now</h2>
  <div class="abs rule" style="top:1578px;left:126px;width:720px;"></div>

  <div class="abs contact phone">
    <svg viewBox="0 0 54 50" fill="none" stroke="var(--gold)" stroke-width="3" stroke-linejoin="round"><path d="M8 3 l10 0 5 12-6 5 c3 7 8 12 15 15 l5-6 12 5 0 10 c0 3-3 5-6 5 C22 49 4 30 3 9 c0-3 2-6 5-6z"/></svg>
    913-555-0148
  </div>
  <div class="abs contact email">
    <svg viewBox="0 0 54 50" fill="none" stroke="var(--gold)" stroke-width="3" stroke-linejoin="round"><rect x="2" y="8" width="50" height="34"/><path d="M2 8 l25 20 25-20 M2 42 l19-17 M52 42 l-19-17"/></svg>
    leasing@northgateholdings.com
  </div>

  <div class="abs sectors">
    <span>Retail</span><span class="dot"></span><span>Restaurant</span><span class="dot"></span><span>Office</span>
  </div>
</main>
</body>
</html>
```